Full Page 40k PSI Water Blasting / Water Jetting Ad

We need a full page ad showing our logo and maybe a few parts we supply. Ad background possibly showing the industries we cater to via picture rather it's a picture of a shipyard, airport runway, industrial plant or oil rig or all four.
- Somewhere on the ad state the following..."Providing Economical Alternatives To The UHP Mobile Water Blasting Industry."
- Maybe add somewhere stating...."When The Pressure&'s Choose BRV."

What has to be on the ad.
- Leading Supplier of Dorwell Stamfry Quelbor Veratube Hose
- Numerous Styles of Sapphire Nozzles
- Wide Variety of Pump and Accessory Replacement Parts
- Brimvale Flow's Own Interchangeable Rotating Spurwand
- Fittings & Adapters
- Safety Gear

Target Market(s)

Contractors, Airport Runway Rubber Removal. Shipyard Waterblasting.

Requirements
Must have
• - Somewhere on the ad state the following..."Providing Economical Alternatives To The UHP Mobile Water Blasting Industry."
• - Maybe add somewhere stating.... "When The Pressure's Choose BRV."
• What has to be on the ad.
• - Leading Supplier of Dorwell Stamfry Quelbor Veratube Hose
• - Numerous Styles of Sapphire Nozzles
• - Wide Variety of Pump and Accessory Replacement Parts
• - Brimvale Flow's Own Interchangeable Rotating Spurwand
• - Fittings & Adapters
• - Safety Gear
Nice to have
• background possibly showing the industries we cater to via picture rather it's a picture of a shipyard, airport runway, industrial plant or oil rig or all four.
• Use a picture of our nozzles off our website.
• www.brimvaleflow.example

```html
<!DOCTYPE html>
<html lang="en">
<head>
<meta charset="utf-8">
<title>Brimvale Flow Technologies – Full Page Ad</title>
<link rel="stylesheet" href="https://fonts.googleapis.com/css2?family=Raleway:wght@300;400;500;700;800&display=swap">
<style>
  :root {
    --stage: #e6e6e6;
    --panel-dark: #454545;
    --brand-blue: #0a8ad8;
    --brand-navy: #1c2f6b;
    --accent-orange: #f5a41c;
    --paper: #ffffff;
    --ink-light: #f2f2f2;
    --logo-panel: #f3f3f3;
  }
  html, body {
    margin: 0;
    width: 1200px;
    height: 1000px;
    overflow: hidden;
    background: var(--stage);
  }
  .ad {
    position: absolute;
    left: 260px;
    top: 20px;
    width: 679px;
    height: 960px;
    box-shadow: 0 6px 18px rgba(0,0,0,0.18);
  }
  .ad svg { display: block; width: 100%; height: 100%; }
  .txt { font-family: 'Raleway', sans-serif; }
  .logo-name { fill: var(--brand-navy); font-weight: 800; font-size: 74px; }
  .logo-company { fill: var(--brand-navy); font-weight: 700; font-size: 19px; }
  .web-url { fill: var(--accent-orange); font-weight: 500; font-size: 25px; }
  .partner-name { fill: var(--paper); font-weight: 800; font-size: 26px; }
  .headline { fill: var(--paper); font-weight: 700; font-size: 42px; }
  .headline-accent { fill: var(--accent-orange); }
  .tagline { fill: var(--ink-light); font-weight: 300; font-size: 32px; }
  .tagline-strong { fill: var(--accent-orange); font-weight: 800; font-size: 30px; }
  .contact-title { fill: var(--accent-orange); font-weight: 700; font-size: 25px; }
  .contact-email { fill: var(--ink-light); font-weight: 400; font-size: 17px; }
  .contact-phone { fill: var(--ink-light); font-weight: 400; font-size: 26px; }
  .feature { fill: var(--ink-light); font-weight: 400; font-size: 22px; }
  .stripe { fill: var(--brand-blue); }
  .hex-frame { fill: var(--paper); stroke: var(--brand-blue); stroke-width: 9; }
</style>
</head>
<body>
<div class="ad">
  <svg viewBox="0 0 948 1340" xmlns="http://www.w3.org/2000/svg">
    <defs>
      <linearGradient id="shipyardTones" x1="0" y1="0" x2="0" y2="1">
        <stop offset="0" stop-color="#d9d9d6"/>
        <stop offset="0.3" stop-color="#8e8c88"/>
        <stop offset="0.45" stop-color="#2a2d33"/>
        <stop offset="0.62" stop-color="#a7261f"/>
        <stop offset="0.8" stop-color="#7a4a30"/>
        <stop offset="1" stop-color="#a07850"/>
      </linearGradient>
      <linearGradient id="productTones" x1="0" y1="0" x2="0" y2="1">
        <stop offset="0" stop-color="#ffffff"/>
        <stop offset="1" stop-color="#e4e4e4"/>
      </linearGradient>
    </defs>

    <!-- Industry photograph area -->
    <rect class="hero-photo" x="0" y="0" width="948" height="960" fill="url(#shipyardTones)"
          role="img" aria-label="Ship in dry dock at a shipyard with cranes and scaffolding"/>

    <!-- Dark lower panel with diagonal top edge -->
    <polygon class="info-panel" points="0,935 948,558 948,1340 0,1340" fill="var(--panel-dark)"/>

    <!-- Logo panel -->
    <polygon class="logo-panel" points="46,0 362,0 362,190 46,330" fill="var(--logo-panel)"/>
    <rect x="108" y="70" width="22" height="22" fill="var(--brand-blue)"/>
    <text class="txt logo-name" x="140" y="140">BRV</text>
    <text class="txt logo-company" x="66" y="192" textLength="266" lengthAdjust="spacingAndGlyphs">Brimvale Flow Technologies, Inc.</text>

    <!-- Accent stripes -->
    <polygon class="stripe" points="66,288 205,230 205,246 66,304"/>
    <polygon class="stripe" points="0,378 293,244 293,266 0,400"/>
    <polygon class="stripe" points="48,872 272,782 272,802 48,892"/>

    <!-- Website -->
    <text class="txt web-url" x="0" y="0" transform="translate(52,958) rotate(-23)" textLength="246" lengthAdjust="spacingAndGlyphs">www.brimvaleflow.example</text>

    <!-- Product hexagons -->
    <g class="product-hex">
      <polygon class="hex-frame" points="264,784 323,682 441,682 500,784 441,886 323,886"/>
      <polygon points="286,784 334,701 430,701 478,784 430,867 334,867" fill="url(#productTones)"
               role="img" aria-label="Rotating water blasting gun with orange grip"/>
    </g>
    <g class="product-hex">
      <polygon class="hex-frame" points="471,699 530,597 648,597 707,699 648,801 530,801"/>
      <polygon points="493,699 541,616 637,616 685,699 637,782 541,782" fill="url(#productTones)"
               role="img" aria-label="Row of threaded sapphire nozzles"/>
    </g>
    <g class="product-hex">
      <polygon class="hex-frame" points="682,614 741,512 859,512 918,614 859,716 741,716"/>
      <polygon points="704,614 752,531 848,531 896,614 848,697 752,697" fill="url(#productTones)"
               role="img" aria-label="Coiled orange high pressure hose with fitting"/>
    </g>

    <!-- Partner name badge -->
    <rect x="740" y="733" width="116" height="44" fill="#000000"/>
    <text class="txt partner-name" x="798" y="764" text-anchor="middle">Dorwell</text>

    <!-- Headline -->
    <text class="txt headline" text-anchor="end">
      <tspan x="905" y="846">WHEN THE</tspan>
      <tspan x="905" y="886">PRESSURE'S ON</tspan>
      <tspan x="905" y="926">CHOOSE <tspan class="headline-accent">BRV.</tspan></tspan>
    </text>

    <!-- Tagline -->
    <text class="txt tagline" x="905" y="993" text-anchor="end">Providing Economical Alternatives To The</text>
    <text class="txt tagline-strong" x="905" y="1033" text-anchor="end">UHP Mobile Water Blasting Industry.</text>

    <!-- Contact -->
    <text class="txt contact-title" x="46" y="1093">CONTACT US</text>
    <text class="txt contact-email" x="46" y="1129" textLength="180" lengthAdjust="spacingAndGlyphs">info@brimvaleflow.example</text>
    <text class="txt contact-phone" x="46" y="1170">555-014-2290</text>
    <rect x="242" y="1073" width="9" height="239" fill="var(--brand-blue)"/>

    <!-- Feature list -->
    <g class="feature-list">
      <circle cx="287" cy="1090" r="3" fill="var(--ink-light)"/>
      <text class="txt feature" x="314" y="1099" textLength="586" lengthAdjust="spacingAndGlyphs">Leading Supplier of Dorwell Stamfry Quelbor Veratube Hose</text>
      <circle cx="287" cy="1130" r="3" fill="var(--ink-light)"/>
      <text class="txt feature" x="314" y="1139">Numerous Styles of Sapphire Nozzles</text>
      <circle cx="287" cy="1170" r="3" fill="var(--ink-light)"/>
      <text class="txt feature" x="314" y="1179">Wide Variety of Pump and Accessory Replacement Parts</text>
      <circle cx="287" cy="1210" r="3" fill="var(--ink-light)"/>
      <text class="txt feature" x="314" y="1219">Brimvale Flow's Own Interchangeable Rotating Spurwand</text>
      <circle cx="287" cy="1250" r="3" fill="var(--ink-light)"/>
      <text class="txt feature" x="314" y="1259">Fittings &amp; Adapters</text>
      <circle cx="287" cy="1290" r="3" fill="var(--ink-light)"/>
      <text class="txt feature" x="314" y="1299">Safety Gear</text>
    </g>
  </svg>
</div>
</body>
</html>
```